olvar stationery

we have a logo and it is in the upload files. Please use the logos in denatured color effect from the same color pantone.
We would like to see a stationery design for a new company working worldwide in the petrochemical sector as an agent.
Please use our logo to create business card, presentation folder, letterhead, envelope,note pad, note books etc etc.
Of course we want convey security and stability, in terms of finance and connections

Target Market(s)

Multinational enterprise, executive, professional,

Industry/Entity Type

Business

Font styles to use
Serif

Colors
0756a3
3176b5
85acd3
86cae6
87c9e5
33a6d7
0692cd

Requirements
Must have
• business cards must have option for address name, title, email telephone etc. I like business card that is both side.

Color as I stated DESAUTERED color effect based on the original color,

I LIKE MATTE effect
Nice to have
• all the pieces must be cohesive. I like print raised for business cards
Should not have
• Shiny finish

```html
<!DOCTYPE html>
<html lang="en">
<head>
<meta charset="utf-8">
<title>Olvar — Stationery</title>
<link href="https://fonts.googleapis.com/css2?family=Cormorant+Garamond:wght@400;500;600&display=swap" rel="stylesheet">
<style>
  :root{
    --backdrop:#e4e5e7;
    --paper:#ffffff;
    --brand:#33a6d7;
    --brand-strong:#0692cd;
    --band:#d5e9f7;
    --ink:#4a4f55;
    --ink-dark:#2d3136;
    --rule:#b9bec4;
    --shadow:0 6px 18px rgba(40,50,60,.12);
  }
  *{box-sizing:border-box;margin:0;padding:0}
  html,body{width:1200px;height:960px;overflow:hidden}
  body{background:var(--backdrop);font-family:"Cormorant Garamond",Georgia,serif;color:var(--ink);position:relative}

  .sheet{position:absolute;background:var(--paper);box-shadow:var(--shadow);overflow:hidden}

  /* Brand block: name only, one colour, one weight */
  .brand-block{position:absolute;top:0;background:var(--brand);display:flex;align-items:center;justify-content:center}
  .brand-name{color:#fff;font-weight:500;letter-spacing:.08em;line-height:1;white-space:nowrap}
  .header-band{position:absolute;top:0;right:0;background:var(--band)}

  /* Footer contact row */
  .contact-row{position:absolute;left:0;right:0;display:flex;justify-content:center}
  .contact-item{display:flex;flex-direction:column;align-items:center;justify-content:center;gap:8px;border-right:1px solid var(--rule);font-size:12px;color:var(--ink);padding:0 14px;white-space:nowrap}
  .contact-item:last-child{border-right:none}
  .contact-item svg{width:14px;height:14px;fill:var(--brand)}
  .base-line{position:absolute;left:0;right:0;bottom:0;height:6px;background:var(--brand)}
  .base-accent{position:absolute;right:0;bottom:0;height:14px;width:24%;background:var(--brand-strong);clip-path:polygon(10px 0,100% 0,100% 100%,0 100%)}

  /* Letterhead */
  .letterhead{left:40px;top:70px;width:566px;height:820px}
  .letterhead .brand-block{left:26px;width:150px;height:58px}
  .letterhead .brand-name{font-size:30px}
  .letterhead .header-band{left:182px;height:66px}
  .letterhead .contact-row{bottom:26px;height:52px}

  /* Envelope */
  .envelope{left:640px;top:70px;width:520px;height:270px}
  .envelope .brand-block{left:22px;width:122px;height:46px}
  .envelope .brand-name{font-size:24px}
  .envelope .header-band{left:150px;height:54px}
  .envelope .contact-row{bottom:20px;height:44px}
  .envelope .contact-item{font-size:10.5px;padding:0 12px;gap:6px}
  .envelope .contact-item svg{width:12px;height:12px}

  /* Business card front */
  .card-front{left:640px;top:400px;width:300px;height:172px;background:var(--brand)}
  .card-front .brand-block{position:static;background:none;height:100%}
  .card-front .brand-name{font-size:40px}

  /* Business card back */
  .card-back{left:640px;top:620px;width:300px;height:172px}
  .card-back .brand-block{left:14px;width:80px;height:30px}
  .card-back .brand-name{font-size:16px}
  .card-back .header-band{left:98px;height:36px}
  .card-back .base-line{height:4px}
  .card-back .base-accent{height:8px;width:22%}
  .card-details{position:absolute;left:16px;top:56px;list-style:none;font-size:8.5px;line-height:1.55}
  .card-details li{display:flex;align-items:center;gap:6px;white-space:nowrap}
  .card-details svg{width:8px;height:8px;fill:var(--brand)}
  .card-person{position:absolute;right:18px;bottom:28px;text-align:right}
  .person-name{font-size:17px;font-weight:600;color:var(--ink-dark);line-height:1}
  .person-title{font-size:10px;font-weight:500;margin-top:3px}
</style>
</head>
<body>

<svg width="0" height="0" style="position:absolute" aria-hidden="true">
  <symbol id="icon-pin" viewBox="0 0 24 24"><path d="M12 2a7 7 0 0 0-7 7c0 5 7 13 7 13s7-8 7-13a7 7 0 0 0-7-7zm0 9.5A2.5 2.5 0 1 1 12 6.5a2.5 2.5 0 0 1 0 5z"/></symbol>
  <symbol id="icon-mail" viewBox="0 0 24 24"><path d="M2 5h20v14H2zm2 2v.5l8 5.5 8-5.5V7zm0 2.9V17h16V9.9l-8 5.5z"/></symbol>
  <symbol id="icon-phone" viewBox="0 0 24 24"><path d="M6.6 10.8a15 15 0 0 0 6.6 6.6l2.2-2.2a1 1 0 0 1 1-.25 11.4 11.4 0 0 0 3.6.57 1 1 0 0 1 1 1V20a1 1 0 0 1-1 1A17 17 0 0 1 3 4a1 1 0 0 1 1-1h3.5a1 1 0 0 1 1 1c0 1.25.2 2.45.57 3.57a1 1 0 0 1-.25 1z"/></symbol>
  <symbol id="icon-web" viewBox="0 0 24 24"><path d="M4 5h16v10H4zm2 2v6h12V7zM1 17h22v2H1z"/></symbol>
</svg>

<section class="sheet letterhead" aria-label="Letterhead">
  <div class="brand-block"><span class="brand-name">Olvar</span></div>
  <div class="header-band"></div>
  <div class="contact-row">
    <div class="contact-item"><svg><use href="#icon-pin"/></svg>office address to be place here</div>
    <div class="contact-item"><svg><use href="#icon-mail"/></svg>info@olvartrading.com</div>
    <div class="contact-item"><svg><use href="#icon-phone"/></svg>+99 999 999 9999</div>
    <div class="contact-item"><svg><use href="#icon-web"/></svg>www.olvartrading.com</div>
  </div>
  <div class="base-line"></div>
  <div class="base-accent"></div>
</section>

<section class="sheet envelope" aria-label="Envelope">
  <div class="brand-block"><span class="brand-name">Olvar</span></div>
  <div class="header-band"></div>
  <div class="contact-row">
    <div class="contact-item"><svg><use href="#icon-pin"/></svg>office address to be place here</div>
    <div class="contact-item"><svg><use href="#icon-mail"/></svg>info@olvartrading.com</div>
    <div class="contact-item"><svg><use href="#icon-phone"/></svg>+99 999 999 9999</div>
    <div class="contact-item"><svg><use href="#icon-web"/></svg>www.olvartrading.com</div>
  </div>
  <div class="base-line"></div>
  <div class="base-accent"></div>
</section>

<section class="sheet card-front" aria-label="Business card front">
  <div class="brand-block"><span class="brand-name">Olvar</span></div>
</section>

<section class="sheet card-back" aria-label="Business card back">
  <div class="brand-block"><span class="brand-name">Olvar</span></div>
  <div class="header-band"></div>
  <ul class="card-details">
    <li><svg><use href="#icon-phone"/></svg>+99 999 999 9999</li>
    <li><svg><use href="#icon-mail"/></svg>info@olvartrading.com</li>
    <li><svg><use href="#icon-web"/></svg>www.olvartrading.com</li>
    <li><svg><use href="#icon-pin"/></svg>office address to be place here</li>
  </ul>
  <div class="card-person">
    <p class="person-name">Adam Hale</p>
    <p class="person-title">Marketing Executive</p>
  </div>
  <div class="base-line"></div>
  <div class="base-accent"></div>
</section>

</body>
</html>
```